依頼概要
■依頼の目的/概要
大型施設の共有スペースに展示する商品のPOPのデザインをお願いします。
展示の全体イメージがありますのでそれに合わせたイメージで制作して下さい。

■依頼詳細
大型SC内の新店舗の商品展示用のPOPになります。
展示イメージに合うようにPOPの制作をして下さい。
前回の展示のPOPを参考にアップしておきますが、同じような配置にする必要はございません。
前回は背景色などは変えずに、商品名、金額等を、レディース、メンズ、キッズの三種類に色分けして区別しておりました。
今回はキッズはないのですが、レディース、メンズ、雑貨と別れておりますので、うまく区別できるような工夫をお願いします。
サイズは A4縦サイズ。
店舗によって商品、金額、アイテム数は変化するので、変更できるような仕様にして下さい。
フォントはモリサワでしたら入っております。
採用後は使用フォントを納品データと共にお知らせください。

■重視する点
Illustrator・Photoshopの経験必須でお願いします。
新店舗のPOPになりますので、」お客様の目に留まるようなデザインが望ましいです。

■継続依頼について
弊社ではこういった案件が多くあり、次回は母の日、父の日等もありますので、継続的依頼できるありがたいです。

その他何かご不明な点がございましたら、お気軽にご質問下さい。
よろしくお願いいたします。
参考用イメージをアップします。

今回の展示イメージ
前回のPOPイメージ

の2点です。
1店舗の最大アイテム数は6になります。
前回のPOP参考例はあくまで参考です。
同じように作作らなくても良いので参考程度にして頂ければ幸いです。
展示イメージにある通り、POPは各マネキン、雑貨の前に置くものになります。
新店舗のオープンなのでワクワクするようなイメージで制作してもらえればと思います。
集まりが少ないので当選額を上乗せします。
それに伴い期間も延長いたします。
ご応募いただきありがとうございました。

見やすくイメージに沿っていたため。

たくさんのご参加ありがとうございました。
ぜひ次回もご参加下さい。

```html
<!DOCTYPE html>
<html lang="ja">
<head>
<meta charset="utf-8">
<title>LADIES タイトル OPEN</title>
<link rel="stylesheet" href="https://fonts.googleapis.com/css2?family=M+PLUS+Rounded+1c:wght@800&family=Noto+Sans+JP:wght@500;700;900&family=Noto+Serif+JP:wght@500;700;900&family=Playfair+Display:ital,wght@0,700;1,700&display=swap">
<style>
  :root {
    --pink-bg: #f3b6d0;
    --pink-stripe: #f8cfe0;
    --pink-deep: #e8388a;
    --pink-shadow: #b8206a;
    --white: #ffffff;
    --purple: #7d3f9e;
    --purple-dark: #5e2b78;
    --red: #d8163c;
    --tag-red: #e0245a;
    --tag-rose: #e23a6e;
    --tag-magenta: #e0408c;
    --ink: #4a2040;
    --grey: #777777;
    --gold-1: #f7e08a;
    --gold-2: #c9982e;
  }
  * { box-sizing: border-box; margin: 0; padding: 0; }
  html, body { width: 843px; height: 1200px; overflow: hidden; }
  body { font-family: "Noto Sans JP", sans-serif; }

  .poster {
    position: relative;
    width: 843px;
    height: 1200px;
    overflow: hidden;
    background:
      repeating-linear-gradient(90deg,
        var(--pink-bg) 0 38px,
        var(--pink-stripe) 38px 48px,
        var(--pink-bg) 48px 60px);
  }
  .backdrop-pattern {
    position: absolute;
    left: 250px; top: 330px;
    width: 343px; height: 720px;
    background: linear-gradient(180deg, rgba(190,110,170,.35), rgba(220,140,190,.25));
  }

  /* header */
  .header {
    position: absolute;
    left: 0; top: 0;
    width: 843px; height: 268px;
    background: var(--white);
    border-bottom: 6px solid #f7d4e4;
    border-radius: 0 0 40px 40px;
  }
  .category-tag {
    position: absolute;
    left: 24px; top: 108px;
    width: 160px; height: 58px;
    background: var(--purple);
    color: var(--white);
    font-family: "Playfair Display", serif;
    font-size: 32px;
    letter-spacing: 3px;
    display: flex; align-items: center; justify-content: center;
    transform: rotate(-12deg);
    border-radius: 4px;
  }
  .title {
    position: absolute;
    left: 176px; top: 44px;
    font-family: "M PLUS Rounded 1c", sans-serif;
    font-size: 108px;
    line-height: 1;
    white-space: nowrap;
    color: var(--pink-deep);
    text-shadow:
      -4px -4px 0 var(--white), 4px -4px 0 var(--white),
      -4px 4px 0 var(--white), 4px 4px 0 var(--white),
      6px 8px 0 var(--pink-shadow);
  }
  .crown-emblem {
    position: absolute;
    left: 630px; top: 70px;
    width: 92px; height: 92px;
    border-radius: 50%;
    background: radial-gradient(circle at 40% 35%, var(--gold-1), var(--gold-2));
    border: 5px solid #f6c6dc;
  }
  .open {
    position: absolute;
    left: 290px; top: 172px;
    font-family: "Playfair Display", serif;
    font-style: italic;
    font-size: 64px;
    line-height: 1.2;
    letter-spacing: 22px;
    color: #8a4a78;
  }

  .appeal {
    position: absolute;
    left: 0; top: 282px;
    width: 843px; height: 58px;
    background: rgba(255,255,255,.85);
    font-size: 22px;
    color: var(--grey);
    padding-left: 82px;
    display: flex; align-items: center;
  }

  /* price cards */
  .price-card {
    position: absolute;
    width: 378px; height: 180px;
    background: var(--white);
    border: 4px solid #f6c3da;
    border-radius: 20px;
  }
  .price-card .item-tag {
    position: absolute;
    left: -8px; top: -22px;
    width: 168px; height: 54px;
    color: var(--white);
    font-size: 30px; font-weight: 700;
    display: flex; align-items: center; justify-content: center;
    transform: rotate(-5deg);
    border-radius: 4px;
  }
  .price-card .item-en {
    position: absolute;
    right: 22px; top: 10px;
    font-family: "Noto Serif JP", serif;
    font-weight: 500;
    font-size: 30px;
    color: var(--ink);
  }
  .price-card .price {
    position: absolute;
    left: 0; right: 0; top: 44px;
    text-align: center;
    font-family: "Noto Serif JP", serif;
    font-weight: 900;
    font-size: 80px;
    line-height: 1;
    color: var(--red);
  }
  .price-card .tax {
    position: absolute;
    left: 0; right: 0; top: 130px;
    text-align: center;
    font-family: "Noto Serif JP", serif;
    font-weight: 500;
    font-size: 30px;
    color: var(--ink);
  }
  .tag-red { background: var(--tag-red); }
  .tag-rose { background: var(--tag-rose); }
  .tag-purple { background: var(--purple); }
  .tag-magenta { background: var(--tag-magenta); }

  .col-left { left: 40px; }
  .col-right { left: 428px; }
  .row-1 { top: 410px; }
  .row-2 { top: 637px; }
  .row-3 { top: 864px; }

  /* footer */
  .store-logo {
    position: absolute;
    left: 34px; top: 1078px;
    width: 236px; height: 80px;
    background: var(--white);
    border: 3px solid var(--ink);
    font-size: 34px; font-weight: 500;
    color: #222;
    display: flex; align-items: center; justify-content: center;
  }
  .store-name {
    position: absolute;
    left: 298px; top: 1066px;
    width: 420px; height: 62px;
    background: var(--purple-dark);
    color: var(--white);
    font-family: "Noto Serif JP", serif;
    font-weight: 700;
    font-size: 32px;
    display: flex; align-items: center;
    padding-left: 22px;
  }
  .floor {
    position: absolute;
    left: 708px; top: 1056px;
    width: 104px; height: 104px;
    border-radius: 50%;
    background: var(--white);
    border: 6px solid var(--purple-dark);
    color: var(--purple-dark);
    font-family: "Noto Sans JP", sans-serif;
    font-weight: 900;
    font-size: 50px;
    display: flex; align-items: center; justify-content: center;
  }
  .corporate-logo {
    position: absolute;
    left: 420px; top: 1134px;
    font-size: 28px; font-weight: 700;
    color: var(--ink);
  }
</style>
</head>
<body>
<main class="poster">
  <div class="backdrop-pattern" role="img" aria-label="Damask ornament pattern in mauve on the pink striped background"></div>

  <header class="header">
    <div class="category-tag">LADIES</div>
    <h1 class="title">タイトル</h1>
    <div class="crown-emblem" role="img" aria-label="Gold round emblem with a crown"></div>
    <div class="open">OPEN</div>
  </header>

  <p class="appeal">アピールコメント</p>

  <section class="price-card col-left row-1">
    <span class="item-tag tag-red">ジャケット</span>
    <span class="item-en">Jacket</span>
    <p class="price">¥4,900</p>
    <p class="tax">税込¥5,292</p>
  </section>
  <section class="price-card col-right row-1">
    <span class="item-tag tag-rose">スカート</span>
    <span class="item-en">Discovering</span>
    <p class="price">¥4,900</p>
    <p class="tax">税込¥5,292</p>
  </section>
  <section class="price-card col-left row-2">
    <span class="item-tag tag-purple">ブラウス</span>
    <span class="item-en">Blouse</span>
    <p class="price">¥4,900</p>
    <p class="tax">税込¥5,292</p>
  </section>
  <section class="price-card col-right row-2">
    <span class="item-tag tag-purple">パンプス</span>
    <span class="item-en">Pumps</span>
    <p class="price">¥4,900</p>
    <p class="tax">税込¥5,292</p>
  </section>
  <section class="price-card col-left row-3">
    <span class="item-tag tag-magenta">ジャケット</span>
    <span class="item-en">Jacket</span>
    <p class="price">¥4,900</p>
    <p class="tax">税込¥5,292</p>
  </section>
  <section class="price-card col-right row-3">
    <span class="item-tag tag-red">スカート</span>
    <span class="item-en">Discovering</span>
    <p class="price">¥4,900</p>
    <p class="tax">税込¥5,292</p>
  </section>

  <footer>
    <div class="store-logo">店舗ロゴ</div>
    <div class="store-name">店舗名 MIRELLE</div>
    <div class="floor">2F</div>
    <div class="corporate-logo">コーポレートロゴ</div>
  </footer>
</main>
</body>
</html>
```